Cannabis & Shroom Informative

Online Blog/Informative website design
Example site: https://leafwardhub.com/

I will need the Ad space as well.

Target Market(s)

Cannabis and (psyho) Mushroom Users

Number of Pages Required

1 page

Colors

Designer to choose colors to be used in the design.

```html
<!DOCTYPE html>
<html lang="en">
<head>
<meta charset="utf-8">
<title>Cannabis &amp; Mushrooms</title>
<link href="https://fonts.googleapis.com/css2?family=Bebas+Neue&family=Open+Sans:wght@400;600;700&family=Poppins:wght@800&display=swap" rel="stylesheet">
<style>
:root{
  --orange:#ff9c00;
  --ink:#1c1c1c;
  --nav-bg:#e6e6e6;
  --panel:#222222;
  --ad:#c2c1bc;
  --ad-line:#8e8d88;
  --white:#ffffff;
  --body:'Open Sans',sans-serif;
  --display:'Bebas Neue',sans-serif;
  --card-title:'Poppins',sans-serif;
}
*{margin:0;padding:0;box-sizing:border-box}
html,body{width:711px;height:1200px;overflow:hidden;background:var(--white)}
.page{position:relative;width:711px;height:1200px;font-family:var(--body);color:var(--ink)}
.abs{position:absolute}

.topbar{left:0;top:0;width:711px;height:32px;background:var(--orange);color:var(--white);font-weight:600;font-size:11px}
.topbar .email{left:24px;top:8px;display:flex;align-items:center;gap:5px}
.topbar .phone{left:298px;top:8px}
.topbar .social{right:18px;top:8px;display:flex;gap:6px}
.social span{width:15px;height:15px;border:1.6px solid var(--white);border-radius:4px;display:block}

.site-title{left:23px;top:58px;font-family:var(--display);font-size:52px;line-height:1;letter-spacing:-.2px;color:var(--ink)}
.ad{background:var(--ad);display:flex;align-items:center;justify-content:center}
.ad b{font-size:10px;font-weight:600;color:#7a7975;border:1px solid var(--ad-line);border-radius:5px;padding:1px 5px;line-height:13px}
.ad-header{left:437px;top:73px;width:248px;height:33px}

.nav{left:0;top:125px;width:711px;height:32px;background:var(--nav-bg)}
.nav a{position:absolute;top:9px;font-size:11px;font-weight:600;color:var(--ink);text-decoration:none;letter-spacing:.1px}

.ticker{left:0;top:157px;width:711px;height:31px;background:var(--orange);color:var(--white);font-weight:600;font-size:11px}
.ticker span{position:absolute;top:8px}
.search{left:577px;top:6px;width:116px;height:20px;background:#f4f4f4;border-radius:4px;color:#9a9a9a;font-weight:400;font-size:10.5px;padding:2px 13px}

.hero-img{left:0;top:188px;width:465px;height:316px;background:radial-gradient(ellipse at 35% 40%,#7a5a32 0%,#3a3520 30%,#1e2314 65%,#141810 100%)}
.hero-panel{left:465px;top:188px;width:246px;height:316px;background:var(--panel);color:var(--white)}
.hero-panel h1{position:absolute;left:18px;top:26px;font-family:var(--display);font-weight:400;font-size:54px;line-height:50px}
.hero-panel .author{position:absolute;left:23px;top:132px;font-size:11.5px;font-weight:700;display:flex;align-items:center;gap:4px}
.hero-panel p{position:absolute;left:19px;top:157px;width:212px;font-size:10.8px;line-height:15.2px}

.section-title{font-family:var(--display);font-size:38px;line-height:1;color:var(--ink)}
.img{position:absolute;height:135px}
.card-title{position:absolute;font-family:var(--card-title);font-weight:800;font-size:17px;line-height:19px;color:var(--ink)}
.card-text{position:absolute;width:210px;font-size:10.8px;line-height:15.2px;color:var(--ink)}
</style>
</head>
<body>
<div class="page">
  <header>
    <div class="abs topbar">
      <div class="abs email">
        <svg width="19" height="14" viewBox="0 0 19 14"><rect x="0.8" y="0.8" width="17.4" height="12.4" fill="none" stroke="#fff" stroke-width="1.5"/><path d="M1 1 L9.5 8 L18 1 M1 13 L7 6.5 M18 13 L12 6.5" fill="none" stroke="#fff" stroke-width="1.3"/></svg>
        hello@sporeleaf.info
      </div>
      <div class="abs phone">Call Us - 999-999-9999</div>
      <div class="abs social" aria-label="Social links"><span></span><span></span><span></span></div>
    </div>

    <div class="abs site-title">CANNABIS &amp; MUSHROOMS</div>
    <div class="abs ad ad-header"><b>AD</b></div>

    <nav class="abs nav">
      <a style="left:24px">HOME</a>
      <a style="left:80px">REVIEWS</a>
      <a style="left:149px">SHOP</a>
      <a style="left:201px">CANNABIS</a>
      <a style="left:278px">MUSHROOMS</a>
      <a style="left:374px">INFORMATION</a>
      <a style="left:472px">ABOUT US</a>
      <a style="left:549px">CONTACT US</a>
    </nav>

    <div class="abs ticker">
      <span style="left:24px">RECENT POSTS</span>
      <span style="left:111px;top:7px"><svg width="8" height="11" viewBox="0 0 8 11"><path d="M2 1.5 L6 5.5 L2 9.5" fill="none" stroke="#fff" stroke-width="1.5"/></svg></span>
      <span style="left:131px">[ January 25, 2020 ] The Newest review of the combined prices</span>
      <span style="left:461px;top:9px"><svg width="10" height="10" viewBox="0 0 10 10"><path d="M0 3.5 H5 V0.5 L9.5 5 L5 9.5 V6.5 H0 Z" fill="#fff"/></svg></span>
      <span style="left:483px">REVIEWS</span>
      <div class="abs search">Search...</div>
    </div>
  </header>

  <section>
    <div class="abs hero-img" role="img" aria-label="Photo of a wild mushroom growing in dark mossy grass"></div>
    <div class="abs hero-panel">
      <h1>MUSHROOM<br>PRICES</h1>
      <div class="author"><svg width="11" height="11" viewBox="0 0 11 11"><circle cx="5.5" cy="3.5" r="2.6" fill="none" stroke="#fff" stroke-width="1"/><path d="M1 10.5 C1 7 10 7 10 10.5" fill="none" stroke="#fff" stroke-width="1"/></svg> Admin</div>
      <p>Lorem ipsum dolor sit amet, consectetur adipiscing elit, sed do eiusmod tempor incididunt ut labore et dolore magna aliqua. Ut enim ad minim veniam, quis nostrud exercitation ullamco laboris nisi ut aliquip ex ea commodo consequat. Duis aute irure dolor in reprehenderit in voluptate velit esse cillum dolore eu fugiat nulla pariatur.</p>
    </div>
  </section>

  <section>
    <h2 class="abs section-title" style="left:23px;top:532px">FEATURED</h2>
    <div class="abs ad" style="left:205px;top:530px;width:471px;height:33px"><b>AD</b></div>

    <div class="img" style="left:24px;top:589px;width:203px;background:linear-gradient(135deg,#c9a27a,#d8c3a0 35%,#b8331f 70%,#8a5a3a)" role="img" aria-label="Photo of mushrooms, tomatoes and green peppers in a pan"></div>
    <div class="img" style="left:251px;top:589px;width:203px;background:linear-gradient(135deg,#2a2a2c,#3a2f2a 50%,#262628)" role="img" aria-label="Photo of colourful leaves on a dark surface"></div>
    <div class="img" style="left:472px;top:589px;width:204px;background:linear-gradient(180deg,#8a8f98,#4a3f35 45%,#2e261f)" role="img" aria-label="Photo of a garden spade in dark soil"></div>

    <h3 class="card-title" style="left:22px;top:738px">Why are Mushroom's<br>prices rising ?</h3>
    <h3 class="card-title" style="left:248px;top:738px">How to check the<br>purity of the leaves ?</h3>
    <h3 class="card-title" style="left:471px;top:738px">5 Creative ways to<br>create manures!</h3>

    <p class="card-text" style="left:22px;top:783px">Lorem ipsum dolor sit amet, consectetur adipiscing elit, sed do eiusmod tempor incididunt ut labore et dolore magna aliqua.</p>
    <p class="card-text" style="left:248px;top:783px">Lorem ipsum dolor sit amet, consectetur adipiscing elit, sed do eiusmod tempor incididunt ut labore et dolore magna aliqua.</p>
    <p class="card-text" style="left:471px;top:783px">Lorem ipsum dolor sit amet, consectetur adipiscing elit, sed do eiusmod tempor incididunt ut labore et dolore magna aliqua.</p>
  </section>

  <section>
    <h2 class="abs section-title" style="left:23px;top:861px">RECOMMENDED</h2>
    <div class="abs ad" style="left:293px;top:858px;width:356px;height:33px"><b>AD</b></div>

    <div class="img" style="left:25px;top:920px;width:203px;background:linear-gradient(160deg,#8a6a50,#b36a3e 45%,#c98a55 80%,#d9a16a)" role="img" aria-label="Photo of brown mushrooms on a wooden board"></div>
    <div class="img" style="left:251px;top:920px;width:201px;background:radial-gradient(ellipse at 50% 55%,#5fae3a,#2f7a25 50%,#1c4a18)" role="img" aria-label="Photo of a green cannabis plant"></div>
    <div class="img" style="left:473px;top:920px;width:203px;background:linear-gradient(160deg,#6a6a66,#4a3e36 50%,#3a2f28)" role="img" aria-label="Photo of a glass jar with dried buds on a desk"></div>

    <h3 class="card-title" style="left:25px;top:1068px">What happens if you<br>don't rinse Mushrooms?</h3>
    <h3 class="card-title" style="left:254px;top:1068px">What do you know<br>about Cannabis?</h3>
    <h3 class="card-title" style="left:478px;top:1068px">How to extract stuff<br>from .... ?</h3>

    <p class="card-text" style="left:25px;top:1114px">Lorem ipsum dolor sit amet, consectetur adipiscing elit, sed do eiusmod tempor incididunt ut labore et dolore magna aliqua.</p>
    <p class="card-text" style="left:254px;top:1114px">Lorem ipsum dolor sit amet, consectetur adipiscing elit, sed do eiusmod tempor incididunt ut labore et dolore magna aliqua.</p>
    <p class="card-text" style="left:477px;top:1114px">Lorem ipsum dolor sit amet, consectetur adipiscing elit, sed do eiusmod tempor incididunt ut labore et dolore magna aliqua.</p>
  </section>
</div>
</body>
</html>
```